Borealis Pictures are looking for a poster design for a new short film called "Paper Lantern"
The film will be submitted to all major film festivals so great exposure....

Paper Lantern was written and directed by Tom Ashworth. Produced by Borealis Pictures. Starring Rob Milner, Clara Whitby, Dan Ashworth, Neil Fairbank and Gareth Pym.

Synopsis: Paper Lantern, tells the story of Joe. A want-away agent/hit man for an undisclosed body, who is sent on a mysterious mission for his final assignment.
Whilst waiting on his last instructions in a hideaway, he meets Magda and Frank and begins to snatch at the real life he's craved for so long.
In danger of taking his eye off the ball too soon, Joe must kill time and fight loneliness, for just one more day.

To give you an feel for the film here is the trailer on Youtube http://www.clipvault-example.net/watch?v=qX7mTz2LpaR.

Please can you put borealis website www.borealispictures-example.co.uk on the design.

Best of luck

```html
<!DOCTYPE html>
<html lang="en">
<head>
<meta charset="utf-8">
<title>Paper Lantern — Poster</title>
<link rel="stylesheet" href="https://fonts.googleapis.com/css2?family=Cinzel:wght@400&family=Crimson+Text:wght@400;600&display=swap">
<style>
  :root {
    --paper: #ffffff;
    --ink-dark: #2e2e30;
    --title: #ffffff;
    --band-red: #d0232a;
    --text-white: #ffffff;
  }
  * { margin: 0; padding: 0; box-sizing: border-box; }
  html, body {
    width: 848px;
    height: 1200px;
    overflow: hidden;
    background: var(--paper);
  }
  .poster {
    position: relative;
    width: 848px;
    height: 1200px;
    background: var(--paper);
    padding: 24px;
  }
  .poster__art {
    position: relative;
    width: 100%;
    height: 100%;
    background: var(--ink-dark);
    overflow: hidden;
  }
  .poster__photo {
    position: absolute;
    inset: 0;
    background:
      /* bright upper-left highlight band */
      radial-gradient(ellipse 34% 11% at 26% 11%, rgba(245,245,245,0.95), rgba(245,245,245,0) 100%),
      radial-gradient(ellipse 45% 16% at 22% 14%, rgba(200,200,200,0.7), rgba(200,200,200,0) 100%),
      /* central bright vertical zone */
      radial-gradient(ellipse 14% 22% at 36% 32%, rgba(240,240,240,0.9), rgba(240,240,240,0) 100%),
      radial-gradient(ellipse 12% 14% at 50% 36%, rgba(215,215,215,0.8), rgba(215,215,215,0) 100%),
      /* left mid-height light */
      radial-gradient(ellipse 18% 10% at 4% 30%, rgba(190,190,190,0.75), rgba(190,190,190,0) 100%),
      /* broad mid-tone head area */
      radial-gradient(ellipse 42% 40% at 36% 36%, rgba(150,150,152,0.85), rgba(150,150,152,0) 100%),
      /* lower mid-tone chin/neck */
      radial-gradient(ellipse 30% 18% at 34% 54%, rgba(120,120,122,0.7), rgba(120,120,122,0) 100%),
      /* darker shadow pocket below centre */
      radial-gradient(ellipse 14% 10% at 30% 43%, rgba(40,40,42,0.6), rgba(40,40,42,0) 100%),
      /* right side grey field */
      linear-gradient(180deg, rgba(110,110,112,0.6) 0%, rgba(80,80,82,0.4) 40%, rgba(0,0,0,0) 75%),
      linear-gradient(95deg, #4a4a4c 0%, #5a5a5c 40%, #4b4b4e 65%, #3a3a3c 100%);
  }
  .poster__shade {
    position: absolute;
    inset: 0;
    background: linear-gradient(to bottom, rgba(30,30,32,0) 0%, rgba(30,30,32,0) 55%, rgba(30,30,32,0.55) 80%, rgba(30,30,32,0.75) 100%);
  }
  .poster__title {
    position: absolute;
    left: 0;
    right: 0;
    top: 858px;
    text-align: center;
    font-family: "Cinzel", "Times New Roman", serif;
    font-weight: 400;
    font-size: 82px;
    line-height: 1;
    letter-spacing: 0.5px;
    color: var(--title);
  }
  .poster__credits {
    position: absolute;
    left: 0;
    right: 0;
    top: 972px;
    text-align: center;
    font-family: "Crimson Text", "Times New Roman", serif;
    font-weight: 600;
    font-size: 14.5px;
    line-height: 20px;
    color: var(--text-white);
  }
  .poster__band {
    position: absolute;
    left: 0;
    right: 0;
    bottom: 0;
    height: 62px;
    background: var(--band-red);
    display: flex;
    align-items: center;
    justify-content: center;
  }
  .poster__url {
    font-family: "Crimson Text", "Times New Roman", serif;
    font-weight: 600;
    font-size: 19px;
    color: var(--text-white);
    letter-spacing: 0.2px;
  }
</style>
</head>
<body>
  <main class="poster">
    <div class="poster__art">
      <div class="poster__photo" role="img" aria-label="Motion-blurred black and white close-up portrait of the lead actor"></div>
      <div class="poster__shade"></div>
      <h1 class="poster__title">Paper Lantern</h1>
      <p class="poster__credits">
        Short film directed by Tom Ashworth. Produced by Borealis Pictures. Starring<br>
        Rob Milner, Clara Whitby, Dan Ashworth, Neil Fairbank and Gareth Pym.
      </p>
      <div class="poster__band">
        <span class="poster__url">www.borealispictures-example.co.uk</span>
      </div>
    </div>
  </main>
</body>
</html>
```